Harrowgate Supply Group Business Card Design

The Business Card will be one side only with Harrowgate Supplies Group Logo
Card should have:
Name
Title
Office phone Number
Cell Number
email address
Website
Street Address
Our Slogan is Rugged and Reliable
Looking for something that stands out from other business cards

Target Market(s)

Heavy equipment Lease Company

```html
<!DOCTYPE html>
<html lang="en">
<head>
<meta charset="utf-8">
<title>Harrowgate Supplies Group – Business Card</title>
<link href="https://fonts.googleapis.com/css2?family=Open+Sans:wght@400;600;700&display=swap" rel="stylesheet">
<style>
  :root {
    --navy: #35378c;
    --navy-dark: #2c2e7a;
    --red: #e52a43;
    --ink: #1c1c24;
    --paper: #f7f7f8;
    --backdrop: #dcdcdc;
  }
  * { box-sizing: border-box; margin: 0; padding: 0; }
  html, body { width: 1200px; height: 864px; overflow: hidden; }
  body {
    background: var(--backdrop);
    font-family: "Open Sans", sans-serif;
    position: relative;
  }
  .card {
    position: absolute;
    width: 660px;
    height: 377px;
    border-radius: 4px;
    box-shadow: 0 6px 18px rgba(0,0,0,.18);
    overflow: hidden;
  }
  /* Front side */
  .card-front { left: 60px; top: 36px; background: var(--paper); }
  .front-brand {
    position: absolute; left: 40px; top: 80px;
    width: 280px;
    display: flex; align-items: center; gap: 12px;
  }
  .brand-mark { width: 26px; height: 26px; background: var(--navy); flex: none; }
  .brand-name {
    font-weight: 700; letter-spacing: .5px;
    line-height: 1.15; text-transform: uppercase;
  }
  .front-brand .brand-name { color: var(--red); font-size: 20px; max-width: 240px; }
  .divider {
    position: absolute; left: 345px; top: 42px;
    width: 2px; height: 196px; background: var(--navy);
  }
  .contact { position: absolute; left: 372px; top: 44px; }
  .contact-name { font-size: 24px; font-weight: 600; color: var(--navy); line-height: 1.1; }
  .contact-title { font-size: 16px; color: var(--red); margin-bottom: 12px; }
  .contact-list { list-style: none; font-size: 15px; color: var(--ink); }
  .contact-list li { display: flex; align-items: flex-start; gap: 8px; line-height: 22px; }
  .contact-list svg { flex: none; width: 15px; height: 15px; margin-top: 3px; }
  .slogan-band {
    position: absolute; left: 0; right: 0; bottom: 0; height: 104px;
    background: var(--navy);
    display: flex; align-items: center; padding-left: 110px;
  }
  .slogan { color: #fff; font-size: 24px; letter-spacing: 1px; }
  /* Back side */
  .card-back {
    left: 480px; top: 449px;
    background: radial-gradient(ellipse at 40% 40%, #3d3f98, var(--navy-dark));
    display: flex; align-items: center; justify-content: center; gap: 18px;
  }
  .card-back .brand-mark { width: 40px; height: 40px; background: #fff; }
  .card-back .brand-name { color: #fff; font-size: 32px; }
</style>
</head>
<body>

<section class="card card-front" aria-label="Business card front">
  <div class="front-brand">
    <span class="brand-mark"></span>
    <span class="brand-name">Harrowgate Supplies Group</span>
  </div>

  <div class="divider"></div>

  <div class="contact">
    <p class="contact-name">Dale Merrick</p>
    <p class="contact-title">Manager</p>
    <ul class="contact-list">
      <li>
        <svg viewBox="0 0 15 15"><rect width="15" height="15" rx="2" fill="var(--navy)"/><rect x="5" y="3" width="5" height="9" rx="1" fill="none" stroke="#fff" stroke-width="1.2"/></svg>
        555 0142.7730
      </li>
      <li>
        <svg viewBox="0 0 15 15"><rect width="15" height="15" rx="2" fill="var(--navy)"/><path d="M4 4c1-1 2 0 2 1s-1 1 0 2.5 2 2 2.5 1 1-1 2 0 0 2-1 2C6 11 3.5 7 4 4z" fill="#fff"/></svg>
        555.019.4418
      </li>
      <li>
        <svg viewBox="0 0 15 15"><rect width="15" height="15" rx="2" fill="var(--navy)"/><rect x="3" y="4.5" width="9" height="6" fill="none" stroke="#fff" stroke-width="1.1"/><path d="M3 4.5l4.5 3.5 4.5-3.5" fill="none" stroke="#fff" stroke-width="1.1"/></svg>
        Merrick@harrowgatesupply.com
      </li>
      <li>
        <svg viewBox="0 0 15 15"><rect width="15" height="15" rx="2" fill="var(--navy)"/><circle cx="7.5" cy="7.5" r="4" fill="none" stroke="#fff" stroke-width="1.1"/><path d="M3.5 7.5h8M7.5 3.5c-2 2.5-2 5.5 0 8M7.5 3.5c2 2.5 2 5.5 0 8" fill="none" stroke="#fff" stroke-width=".9"/></svg>
        www.HarrowgateSupply.com
      </li>
      <li>
        <svg viewBox="0 0 15 15"><rect width="15" height="15" rx="2" fill="var(--navy)"/><path d="M7.5 12.5S4 8.5 4 6.3a3.5 3.5 0 0 1 7 0c0 2.2-3.5 6.2-3.5 6.2z" fill="#fff"/><circle cx="7.5" cy="6.3" r="1.2" fill="var(--navy)"/></svg>
        <span>Sample Location<br>D.B.A. Ridgeway Rentals<br>Larkfield, CA 95400</span>
      </li>
    </ul>
  </div>

  <div class="slogan-band">
    <p class="slogan">Rugged and Reliable</p>
  </div>
</section>

<section class="card card-back" aria-label="Business card back">
  <span class="brand-mark"></span>
  <span class="brand-name">Harrowgate Supplies Group</span>
</section>

</body>
</html>
```